Varemo Group Business Card Design

The CEO is looking for a new trendy look for his business card.
You can stay with current branding or come up with something new/creative. It can be 3D, including Medical Office buildings. You can use our logo in a variety of colors. Please include name, title, company name, company website, email address, cell number

Target Market(s)

Real Estate Development and Construction

Industry/Entity Type

Health care real estate

Contact Information for Business Card

Rohesh Kumbar, CEO M-727.418.9062 E-roheshkumbar@varemo.com Address:4100 Lindell Ave, Tampa, FL 33611 www.varemo.com

Font styles to use
Other font styles liked:
• Be creative

Requirements
Must have
• Creative, trendy look
Nice to have
• Please go to our website to get a feel- www. varemo.com
Should not have
• small fonts

```html
<!DOCTYPE html>
<html lang="en">
<head>
<meta charset="utf-8">
<title>Varemo Group Business Card</title>
<link rel="stylesheet" href="https://fonts.googleapis.com/css2?family=Poppins:wght@300;600;800&display=swap">
<style>
  :root {
    --page-bg: #e4e4e6;
    --card-bg: #ffffff;
    --card-shade: #ededee;
    --ink-black: #1c1c1c;
    --brand-red: #9b1b24;
    --brand-navy: #1d2a44;
    --text-grey: #4a4a4a;
    --watermark: #ececec;
    --rule: #9a9a9a;
  }
  * { margin: 0; padding: 0; box-sizing: border-box; }
  html, body {
    width: 1200px; height: 900px; overflow: hidden;
    background: var(--page-bg);
    font-family: "Poppins", sans-serif;
  }
  .card {
    position: absolute;
    left: 280px;
    width: 640px; height: 366px;
    background: linear-gradient(120deg, var(--card-shade) 0%, var(--card-bg) 70%);
    box-shadow: 0 10px 28px rgba(0,0,0,0.18);
    overflow: hidden;
  }
  .card--front { top: 60px; }
  .card--back { top: 470px; }

  .side-mark {
    position: absolute;
    right: -118px; top: 150px;
    transform: rotate(90deg);
    font-weight: 800;
    font-size: 92px;
    letter-spacing: -2px;
    color: var(--watermark);
    white-space: nowrap;
    line-height: 1;
  }

  .brand-name {
    font-weight: 800;
    letter-spacing: -1.5px;
    line-height: 1;
    white-space: nowrap;
  }
  .card--front .brand-name {
    position: absolute; left: 70px; top: 148px;
    font-size: 62px; color: var(--ink-black);
  }
  .card--back .brand-name {
    position: absolute; left: 42px; top: 44px;
    font-size: 44px; color: var(--brand-red);
  }

  .person { position: absolute; left: 86px; top: 168px; }
  .person__name { font-weight: 600; font-size: 22px; color: var(--brand-red); line-height: 1.2; }
  .person__title { font-weight: 300; font-size: 16px; color: var(--text-grey); padding-left: 14px; }

  .contact-list {
    position: absolute; left: 100px; top: 250px;
    list-style: none;
    font-weight: 300; font-size: 16px; color: var(--text-grey);
  }
  .contact-list li { display: flex; align-items: center; gap: 10px; height: 26px; }
  .contact-list svg { width: 16px; height: 16px; flex: none; }

  .address {
    position: absolute; left: 420px; top: 250px;
    padding-left: 14px;
    border-left: 1px solid var(--rule);
    font-weight: 300; font-size: 16px; color: var(--text-grey);
    line-height: 26px;
  }
</style>
</head>
<body>
  <section class="card card--front" aria-label="Card front">
    <div class="side-mark" aria-hidden="true">Varemo</div>
    <div class="brand-name">Varemo Group</div>
  </section>

  <section class="card card--back" aria-label="Card back">
    <div class="side-mark" aria-hidden="true">Varemo</div>
    <div class="brand-name">Varemo Group</div>

    <div class="person">
      <div class="person__name">Rohesh Kumbar</div>
      <div class="person__title">CEO</div>
    </div>

    <ul class="contact-list">
      <li>
        <svg viewBox="0 0 16 16" aria-hidden="true"><rect x="4" y="1" width="8" height="14" rx="1.5" fill="none" stroke="#1d2a44" stroke-width="1.4"/><line x1="7" y1="12.5" x2="9" y2="12.5" stroke="#1d2a44" stroke-width="1.2"/></svg>
        727.418.9062
      </li>
      <li>
        <svg viewBox="0 0 16 16" aria-hidden="true"><circle cx="8" cy="8" r="6.5" fill="none" stroke="#1d2a44" stroke-width="1.3"/><ellipse cx="8" cy="8" rx="3" ry="6.5" fill="none" stroke="#1d2a44" stroke-width="1"/><line x1="1.5" y1="8" x2="14.5" y2="8" stroke="#1d2a44" stroke-width="1"/></svg>
        www.varemo.com
      </li>
      <li>
        <svg viewBox="0 0 16 16" aria-hidden="true"><rect x="1" y="3.5" width="14" height="9" fill="#1d2a44"/><polyline points="1,3.5 8,9 15,3.5" fill="none" stroke="#ffffff" stroke-width="1"/></svg>
        roheshkumbar@varemo.com
      </li>
    </ul>

    <address class="address" style="font-style:normal">
      4100 Lindell Ave<br>
      Tampa, FL 33611
    </address>
  </section>
</body>
</html>
```